New management consulting website

I need a 4-5 page website that I can manage in WordPress on Hostlane.example for a new management consulting company. The website is www.torvik-example.com and the company name is Torvik Group LLC. The attached spec has an example of a draft site, layout and actual copy and includes company and contact information. I have more high-res images I can send.

Must include instruction/assistance loading the site to my WordPress dashboard.

Target Market(s)

Any business, especially SAAS

Industry/Entity Type

Consultant

Coding

Coded - Design and coding required

Number of Pages Required

4 page

Font styles to use
Sans Serif

Colors
0456a4

Requirements
Must have
• Modern and stylish

```html
<!DOCTYPE html>
<html lang="en">
<head>
<meta charset="utf-8">
<title>Contact Us – Torvik Consulting</title>
<link href="https://fonts.googleapis.com/css2?family=Lato:ital,wght@0,400;0,700;1,400&family=Michroma&display=swap" rel="stylesheet">
<style>
:root{
  --navy:#1d3f6b;
  --navy-dark:#1a3c66;
  --ink:#222;
  --muted:#555;
  --icon:#8a8a8a;
  --rule:#b5b5b5;
  --field:#a9a9a9;
  --footer-bar:#8f9094;
  --white:#fff;
}
*{margin:0;padding:0;box-sizing:border-box}
html,body{width:1200px;height:2479px;overflow:hidden;background:var(--white)}
body{position:relative;font-family:"Lato",sans-serif;color:var(--ink)}
.abs{position:absolute}
.display{font-family:"Michroma",sans-serif}

/* header */
.site-header{left:0;top:0;width:1200px;height:102px}
.brand{left:118px;top:30px;font-family:"Lato",sans-serif;font-weight:700;font-size:30px;letter-spacing:1px;color:var(--navy);line-height:1}
.brand small{display:block;font-size:10px;letter-spacing:2px;font-weight:400;margin-top:2px;text-align:center}
.main-nav{top:48px;display:flex;gap:0;font-size:14px}
.main-nav a{position:absolute;color:var(--ink);text-decoration:none;white-space:nowrap}
.main-nav a.active{color:var(--navy)}
.nav-marker{left:833px;top:34px;width:22px;height:3px;background:#999}
.btn{background:var(--navy-dark);color:var(--white);font-size:14px;display:flex;align-items:center;justify-content:center;text-decoration:none}
.quote-btn{left:930px;top:35px;width:158px;height:43px}

/* hero */
.hero{left:0;top:102px;width:1200px;height:384px;
  clip-path:polygon(0 0,100% 0,100% 100%,0 85%);
  background:linear-gradient(180deg,#cfe9ea 0%,#8fc4c6 45%,#5d8d88 75%,#6b5a3e 100%)}
.hero h1{position:absolute;left:0;width:1200px;top:150px;text-align:center;font-family:"Michroma",sans-serif;font-weight:400;font-size:34px;color:var(--white);letter-spacing:1px}

/* contact section */
.section-title{left:0;width:1200px;text-align:center;color:var(--navy);font-weight:400}
.rule{height:2px;background:var(--rule);width:28px}
.info-col{width:220px;text-align:center}
.info-col h3{font-size:18px;font-weight:700;color:var(--navy);margin:10px 0 16px}
.info-col p{font-size:13.5px;line-height:17px;color:var(--ink)}
.divider{width:1px;background:#ccc;top:620px;height:108px}

/* form */
.intro{left:0;width:1200px;top:865px;text-align:center;font-size:13.5px}
.field{left:324px;width:555px;border:1px solid var(--field);font-size:13px;font-style:italic;color:#999;padding:0 20px;display:flex;align-items:center}
.field.message{align-items:flex-start;padding-top:14px}
.send-btn{left:523px;top:1215px;width:157px;height:43px}

/* social */
.social{top:1447px;width:40px;height:32px;display:flex;align-items:center;justify-content:center;color:var(--navy);font-size:11px;font-weight:700}

/* map */
.map{left:0;top:1523px;width:1200px;height:611px;
  clip-path:polygon(0 0,100% 15%,100% 100%,0 100%);
  background:linear-gradient(180deg,#f1f2f4,#e9ebee)}

/* footer */
.site-footer{left:0;top:2134px;width:1200px;height:302px;background:var(--navy)}
.footer-brand{left:111px;top:2260px;color:var(--white);font-weight:700;font-size:44px;letter-spacing:2px;line-height:1;text-align:center}
.footer-brand small{display:block;font-size:14px;letter-spacing:3px;font-weight:700;margin-top:2px}
.footer-col h4{font-family:"Michroma",sans-serif;font-weight:400;font-size:13px;color:var(--white);letter-spacing:.5px}
.footer-col .rule{background:#8aa3c4;margin-top:9px;width:56px}
.footer-col ul{list-style:none;margin-top:22px}
.footer-col li{font-size:13.5px;line-height:21px;color:var(--white)}
.contact-line{display:flex;gap:14px;color:var(--white);font-size:13.5px;line-height:16px}
.contact-line svg{flex:none}
.copyright{left:0;top:2436px;width:1200px;height:43px;background:var(--footer-bar);color:var(--white);font-size:13.5px;display:flex;align-items:center;justify-content:center}
</style>
</head>
<body>

<header class="abs site-header">
  <div class="abs brand">TORVIK<small>CONSULTING</small></div>
  <nav class="main-nav">
    <a class="abs" style="left:562px;top:48px" href="#">HOME</a>
    <a class="abs" style="left:638px;top:48px" href="#">ABOUT</a>
    <a class="abs" style="left:719px;top:48px" href="#">SERVICES</a>
    <a class="abs active" style="left:813px;top:48px" href="#">CONTACT</a>
  </nav>
  <div class="abs nav-marker"></div>
  <a class="abs btn quote-btn" href="#">GET A QUOTE</a>
</header>

<section class="abs hero" role="img" aria-label="Misty teal mountain range landscape">
  <h1>CONTACT US</h1>
</section>

<h2 class="abs section-title display" style="top:520px;font-size:25px">GET IN TOUCH WITH US</h2>
<div class="abs rule" style="left:573px;top:574px"></div>

<div class="abs info-col" style="left:258px;top:618px">
  <svg width="34" height="34" viewBox="0 0 24 24" fill="var(--icon)"><path d="M20 2c-1 0-2 .6-2.4 1.4l-1.2 2.4c-.4.8-.1 1.7.6 2.1l.8.5c-1.3 3-3.6 5.3-6.6 6.6l-.5-.8c-.4-.7-1.3-1-2.1-.6l-2.4 1.2C5.6 15.3 5 16.1 5 17l.2 2c2 0 9-2.4 13-8.5C20 7.8 21 5 21 3z" transform="rotate(10 12 12)"/></svg>
  <h3>Phone</h3>
  <p>555-014-0192</p>
</div>
<div class="abs divider" style="left:463px"></div>
<div class="abs info-col" style="left:490px;top:618px">
  <svg width="28" height="30" viewBox="0 0 24 24" fill="var(--icon)"><path d="M12 2a7 7 0 0 0-7 7c0 5 7 13 7 13s7-8 7-13a7 7 0 0 0-7-7zm0 9.5A2.5 2.5 0 1 1 12 6.5a2.5 2.5 0 0 1 0 5z"/></svg>
  <h3>Address</h3>
  <p>742 Harlow Ave<br>#210, Springfield, ST 00000</p>
</div>
<div class="abs divider" style="left:733px"></div>
<div class="abs info-col" style="left:722px;top:618px">
  <svg width="28" height="26" viewBox="0 0 24 20" fill="var(--icon)"><path d="M2 3h20v2l-10 6L2 5z M2 7.5l10 6 10-6V17H2z"/></svg>
  <h3>Email</h3>
  <p>info@torvik-example.com</p>
</div>

<p class="abs intro">Have any questions? We`d love to hear from you.</p>
<div class="abs field" style="top:903px;height:40px">Full name</div>
<div class="abs field" style="top:959px;height:40px">Phone#</div>
<div class="abs field" style="top:1013px;height:40px">Email Address</div>
<div class="abs field message" style="top:1070px;height:126px">Message*</div>
<a class="abs btn send-btn" href="#">SEND NOW</a>

<h2 class="abs section-title" style="top:1352px;font-size:27px;font-weight:700">Connect with us</h2>
<div class="abs rule" style="left:575px;top:1407px"></div>

<a class="abs social" style="left:508px" href="#">Social</a>
<div class="abs social" style="left:581px">
  <svg width="28" height="22" viewBox="0 0 24 19" fill="var(--navy)"><path d="M1 2h22v2.5L12 11 1 4.5z M1 7l11 6.5L23 7v11H1z"/></svg>
</div>
<a class="abs social" style="left:652px" href="#">Reviews</a>

<div class="abs map" role="img" aria-label="Street map showing the office location"></div>

<footer class="abs site-footer"></footer>
<div class="abs footer-brand">TORVIK<small>CONSULTING</small></div>

<div class="abs footer-col" style="left:442px;top:2206px">
  <h4>CONTACT INFO.</h4>
  <div class="rule"></div>
  <div class="contact-line" style="margin-top:30px">
  <svg width="16" height="18" viewBox="0 0 24 24" fill="#8aa3c4"><path d="M12 2a7 7 0 0 0-7 7c0 5 7 13 7 13s7-8 7-13a7 7 0 0 0-7-7zm0 9.5A2.5 2.5 0 1 1 12 6.5a2.5 2.5 0 0 1 0 5z"/></svg>
  <span>742 Harlow Ave<br>#210, Springfield, ST 00000</span></div>
  <div class="contact-line" style="margin-top:14px">
  <svg width="16" height="14" viewBox="0 0 24 19" fill="#8aa3c4"><path d="M1 2h22v2.5L12 11 1 4.5z M1 7l11 6.5L23 7v11H1z"/></svg>
  <span>info@torvik-example.com</span></div>
  <div class="contact-line" style="margin-top:16px">
  <svg width="16" height="16" viewBox="0 0 24 24" fill="#8aa3c4"><path d="M20 2c-1 0-2 .6-2.4 1.4l-1.2 2.4c-.4.8-.1 1.7.6 2.1l.8.5c-1.3 3-3.6 5.3-6.6 6.6l-.5-.8c-.4-.7-1.3-1-2.1-.6l-2.4 1.2C5.6 15.3 5 16.1 5 17l.2 2c2 0 9-2.4 13-8.5C20 7.8 21 5 21 3z"/></svg>
  <span>Tel: 555-014-0192</span></div>
</div>

<div class="abs footer-col" style="left:752px;top:2206px">
  <h4>QUICK LINKS</h4>
  <div class="rule"></div>
  <ul><li>Home</li><li>About</li><li>Services</li><li>Contact</li></ul>
</div>

<div class="abs footer-col" style="left:971px;top:2206px">
  <h4>USEFUL LINKS</h4>
  <div class="rule"></div>
  <ul><li>Privacy policy</li><li>Terms &amp; conditions</li></ul>
</div>

<div class="abs copyright">© 2021 Torvik Group LLC | All Rights Reserved</div>

</body>
</html>
```